Bifold brochure design for leadership academy

Please see below. This is a bifold brochure for a leadership academy. (www.vesk.institute). Look and feel must be colours, shapes, abstract designs, graphics, pictures. Make this professional, yet casual and bold.

Feel free to design just the front and back cover, then I'll give feedback on whether or not you're in the right direction.

COVER
- Title: “The Brightwater Year Journey”
- “Northmere Pathways Institute” logo somewhere
- Subtitles (with images, icons, and/or shapes): “Self-discovery” “Skills development” “Real-world Impact”

PAGE 2 (Inside Fold)
- Title: "The Program"
- Section 2a: Section title: "How it works”
- Image: See website, image under "four phases of the program". Please adapt and make it look better
- Text: VPI is a structured, 8-month ‘gap year’ program for 18-25 year olds who want more than just a year off – they want a year ahead. Our aim is to develop high-potential young leaders with strong values, clear purpose, high-impact skills, and a track record of real-world accomplishments that are second-to-none. We do this through four-phases.
- Section 2b: Section title: “Dates & Timing”
- Image: See image on website under 'dates and timing'. Make sure both dates show up on the brochure (September and January program).
- Text: There are two programs per year: one that starts in September, the other in January. The first four months of the program are based in Toronto at the VPI headquarters. The curriculum we work through is highly engaging and personalized, focusing directly on students’ goals. After that, students are out in the world, achieving the remaining components of the program (e.g. internship, volunteer abroad).

PAGE 3 (Outside Fold)
- Page Title: "The Students"
- Section 3a: Section title: “Who’s it for”
- Subtitle1: “High school graduates”
 Image/icon of a high school grad
 Text1: 90% of high school grads aren't sure why they’re going to university or what they want to study.
 Text2: VPI helps students discover what they truly want to do in life, and make enormous progress towards these goals.

- Subtitle2: “Post-secondary students”
 Image/icon of a university / college student
 Text1: 28% of students switch or drop out of their program because it wasn’t for them or they didn’t like it.
 Text2: Don't keep moving around or risk switching careers down the road – find out what sparks your passion with VPI.

- Subtitle3: “Post-secondary graduates”
 Image/icon of a university/ college grad
 Text1: 50% of graduates are unemployed or underemployed, 60% are in debt.
 Text2: VPI will help you get your dream job – our students won’t settle for anything less.

- Section 3b: Section title: “How to apply”
 Text1: We select high-potential young leaders with a desire to improve themselves and impact the world.
 Text2: We won’t ask you for your grades – we care more about your values and potential.
 Text3: Visit www.vesk.institute to apply now

BACK COVER
- Page Title: “Get in Touch”
- Website: www.vesk.institute
- Facebook page: facebook.com/vesk.institute
- Twitter handle: @vesk_institute
- Email: marta@vesk.institute

Target Market(s)

18-25 year olds, parents, teachers

Industry/Entity Type

Leadership

Requirements
Must have
• Beautiful design - sleek and bold, yet colourful and casual. Keep the colours similar to our website (www.vesk.institute). See examples of other brochures.
• http://img.plorvex.net/jpg/00/11/22/33/240_F_11223344_aBcDeFgHiJkLmNoPqRsTuVwXyZ123456.jpg
• http://quandrelhub.com/wp-content/uploads/2014/11/Real-Estate-Bi-fold-Brochure.jpg
• http://www.trovanic.com/media/k2/galleries/5/001-bi-fold-brochure-psd-mock-up-template.jpg
• http://img.plorvex.net/jpg/00/44/55/66/240_F_44556677_zYxWvUtSrQpOnMlKjIhGfEdCbA987654.jpg

```html
<!DOCTYPE html>
<html lang="en">
<head>
<meta charset="utf-8">
<title>The Program / The Students</title>
<link href="https://fonts.googleapis.com/css2?family=Source+Sans+3:wght@300;400;600;700&display=swap" rel="stylesheet">
<style>
:root{
  --paper:#ffffff;
  --ink:#4d4d4f;
  --ink-dark:#2f2f31;
  --heading:#c3662b;
  --title-blue:#3f7fc2;
  --phase-green:#7b8f4d;
  --phase-green-soft:#c9d3ad;
  --phase-grey:#9a9a9a;
  --phase-grey-soft:#e3e3e3;
  --phase-blue:#2f4b9b;
  --phase-blue-soft:#c6d3ea;
  --phase-red:#c2433b;
  --phase-red-soft:#f2d2cd;
  --timeline-bg:#f4e4c9;
  --bar-red:#c9433a;
  --bar-blue:#2f4b9b;
  --icon-blue:#3b6fc0;
  --icon-red:#b13a2f;
  --icon-sky:#cfe2f3;
  --bullet:#b8b8b8;
}
*{box-sizing:border-box;margin:0;padding:0}
html,body{width:1200px;height:927px;overflow:hidden;background:var(--paper)}
body{position:relative;font-family:"Source Sans 3",Arial,sans-serif;color:var(--ink)}
.spread{position:absolute;inset:0}
.page-title{position:absolute;font-weight:300;font-size:32px;letter-spacing:2px;color:var(--title-blue);white-space:nowrap;text-transform:uppercase}
.page-title--program{left:40px;top:278px;transform-origin:0 0;transform:rotate(-90deg)}
.page-title--students{left:1160px;top:66px;transform-origin:0 0;transform:rotate(90deg)}
.section-heading{position:absolute;font-weight:700;font-size:18.5px;color:var(--heading)}
.body-copy{position:absolute;font-size:14.4px;line-height:20px;color:var(--ink)}
.phases{position:absolute;left:95px;top:220px;width:445px;height:210px}
.phase{position:absolute;top:0;width:101px}
.phase__label{height:20px;color:#fff;font-size:11px;font-weight:700;padding:3px 5px}
.phase__body{padding:6px 6px;font-size:6.4px;line-height:8px;color:#444}
.phase__art{height:64px;margin:2px 6px 6px}
.phase--discover{left:0}
.phase--discover .phase__label{background:var(--phase-green)}
.phase--discover .phase__body{background:var(--phase-green-soft);height:125px}
.phase--design{left:101px}
.phase--design .phase__label{background:var(--phase-grey)}
.phase--design .phase__body{background:var(--phase-grey-soft);height:132px}
.phase--build{left:202px}
.phase--build .phase__label{background:var(--phase-blue)}
.phase--build .phase__body{background:var(--phase-blue-soft);height:140px}
.phase--achieve{left:303px;width:101px}
.phase--achieve .phase__label{background:var(--phase-red)}
.phase--achieve .phase__body{background:var(--phase-red-soft);height:208px}
.achieve-list{list-style:none;margin-top:4px}
.achieve-list li{display:flex;align-items:center;gap:4px;margin:3px 0}
.achieve-list li::before{content:"";width:6px;height:6px;border-radius:50%;background:var(--phase-red);flex:none}
.timeline{position:absolute;left:95px;top:600px;width:442px;height:285px}
.icon-tile{position:absolute;left:637px;width:90px;height:86px;border-radius:9px}
.sub-heading{position:absolute;font-weight:700;font-size:14.4px;color:var(--ink-dark)}
.bullets{position:absolute;list-style:none;width:312px;font-size:14.4px;line-height:20px}
.bullets li{position:relative;padding-left:12px;margin-bottom:10px}
.bullets li::before{content:"";position:absolute;left:1px;top:8px;width:5px;height:5px;border-radius:50%;background:var(--bullet)}
</style>
</head>
<body>
<main class="spread">

  <!-- Left page: The Program -->
  <h1 class="page-title page-title--program">The Program</h1>

  <h2 class="section-heading" style="left:95px;top:66px">How it works</h2>
  <p class="body-copy" style="left:95px;top:94px;width:495px">VPI is a structured, 8-month ‘gap year’ program for 18-25 year olds who want more than just a year off – they want a year ahead. Our aim is to develop high-potential young leaders with strong values, clear purpose, high-impact skills, and a track record of real-world accomplishments that are second-to-none.<br>We do this through four-phases.</p>

  <section class="phases">
    <div class="phase phase--discover">
      <div class="phase__label">1. Discover</div>
      <div class="phase__body">
        <div class="phase__art" role="img" aria-label="Compass illustration" style="background:radial-gradient(circle,#7fa6c9 0 40%,#a9b98a 70%)"></div>
        Discover your strengths, growth areas, personality, core values and other traits through a personal transformation program.
      </div>
    </div>
    <div class="phase phase--design">
      <div class="phase__label">2. Design</div>
      <div class="phase__body">
        <div class="phase__art" role="img" aria-label="Goals sheet illustration" style="background:linear-gradient(#f7f7f7,#cfcfcf)"></div>
        Design your personal plan and set clear goals through our structured goal-setting process.
      </div>
    </div>
    <div class="phase phase--build">
      <div class="phase__label">3. Build</div>
      <div class="phase__body">
        <div class="phase__art" role="img" aria-label="Classroom workshop illustration" style="background:linear-gradient(#e9dfc6,#9fb4d8)"></div>
        Build real-world skills that matter through workshops, projects, mentorship and hands-on practice.
      </div>
    </div>
    <div class="phase phase--achieve">
      <div class="phase__label">4. Achieve</div>
      <div class="phase__body">
        <div class="phase__art" role="img" aria-label="Achievement icons illustration" style="height:44px;background:linear-gradient(90deg,#e8b04a,#c9433a,#9cc3e0)"></div>
        Achieve real things when you are out in the world:
        <ul class="achieve-list">
          <li>Solve a social problem</li>
          <li>Conquer a physical feat</li>
          <li>Volunteer abroad</li>
          <li>Do an internship</li>
          <li>Organize an event</li>
          <li>Start something</li>
        </ul>
      </div>
    </div>
  </section>

  <h2 class="section-heading" style="left:95px;top:430px">Dates &amp; Timing</h2>
  <p class="body-copy" style="left:95px;top:458px;width:495px">There are two programs per year: one that starts in September, the other in January. The first four months of the program are based in Toronto at the VPI headquarters. The curriculum we work through is highly engaging and personalized, focusing directly on students’ goals. After that, students are out in the world, achieving the remaining components of the program (e.g. internship, volunteer abroad).</p>

  <svg class="timeline" viewBox="0 0 295 190" font-family="Source Sans 3, Arial, sans-serif">
    <rect x="0" y="0" width="295" height="190" rx="12" fill="var(--timeline-bg)"/>
    <g font-size="3.6" fill="#555" font-weight="600">
      <text x="6" y="7">PREPARING</text><text x="8" y="11">ONLINE</text>
      <text x="50" y="10">FULL-TIME (TORONTO)</text>
      <text x="166" y="10">ABROAD (CHECKPOINT)</text>
    </g>
    <line x1="32" y1="7" x2="127" y2="7" stroke="#777" stroke-width=".4"/>
    <line x1="130" y1="7" x2="238" y2="7" stroke="#777" stroke-width=".4"/>
    <g font-size="7" fill="#444" text-anchor="middle">
      <text x="12" y="20">Aug</text><text x="37" y="20">Sep</text><text x="63" y="20">Oct</text>
      <text x="89" y="20">Nov</text><text x="115" y="20">Dec</text><text x="141" y="20">Jan</text>
      <text x="166" y="20">Feb</text><text x="192" y="20">Mar</text><text x="217" y="20">Apr</text>
      <text x="242" y="20">May</text><text x="268" y="20">Jun</text><text x="290" y="20">Jul</text>
    </g>
    <line x1="4" y1="24" x2="291" y2="24" stroke="#888" stroke-width=".6"/>
    <!-- Discover -->
    <rect x="8" y="30" width="14" height="12" fill="#333"/>
    <text x="9.5" y="38.5" font-size="6" font-weight="700" fill="#fff">VPI</text>
    <rect x="24" y="33" width="48" height="8" fill="var(--bar-blue)"/>
    <text x="28" y="38.5" font-size="3.8" fill="#fff">Find your purpose</text>
    <!-- Design -->
    <circle cx="30" cy="57" r="7" fill="#8aa5c0" stroke="#556" stroke-width=".5"/>
    <rect x="38" y="56" width="22" height="7" fill="var(--bar-blue)"/>
    <text x="40" y="60.8" font-size="3.6" fill="#fff">Set goals</text>
    <!-- Build -->
    <rect x="22" y="80" width="96" height="8" fill="var(--bar-blue)"/>
    <text x="26" y="85.5" font-size="4" fill="#fff" font-weight="700">BUILD</text>
    <text x="50" y="85.5" font-size="3.6" fill="#fff">Core skills training</text>
    <text x="128" y="77" font-size="3.6" fill="#2f4b9b" font-weight="700">MONTHLY CHECKPOINTS</text>
    <g fill="var(--bar-blue)">
      <rect x="138" y="80" width="4" height="8"/><rect x="163" y="80" width="4" height="8"/>
      <rect x="189" y="80" width="4" height="8"/><rect x="214" y="80" width="4" height="8"/>
      <rect x="239" y="80" width="4" height="8"/>
    </g>
    <!-- Achieve -->
    <circle cx="30" cy="103" r="7" fill="var(--bar-red)"/>
    <rect x="36" y="99" width="70" height="8" fill="var(--bar-red)"/>
    <text x="40" y="104.5" font-size="3.8" fill="#fff">Solve a social problem</text>
    <circle cx="182" cy="122" r="6" fill="#555"/>
    <rect x="188" y="118" width="52" height="8" fill="var(--bar-red)"/>
    <text x="192" y="123.5" font-size="3.8" fill="#fff">Do an internship</text>
    <circle cx="28" cy="145" r="7" fill="#e6a53a"/>
    <rect x="34" y="141" width="78" height="8" fill="var(--bar-red)"/>
    <text x="38" y="146.5" font-size="3.8" fill="#fff">Conquer a physical feat</text>
    <circle cx="125" cy="145" r="6" fill="#2f4b9b"/>
    <rect x="131" y="141" width="52" height="8" fill="var(--bar-red)"/>
    <text x="135" y="146.5" font-size="3.8" fill="#fff">Volunteer abroad</text>
    <circle cx="35" cy="168" r="7" fill="var(--bar-red)"/>
    <rect x="41" y="164" width="50" height="8" fill="var(--bar-red)"/>
    <text x="45" y="169.5" font-size="3.8" fill="#fff">Organize an event</text>
    <circle cx="125" cy="167" r="6" fill="#333"/>
    <rect x="131" y="163" width="66" height="8" fill="var(--bar-red)"/>
    <text x="135" y="168.5" font-size="3.8" fill="#fff">Start something</text>
  </svg>

  <!-- Right page: The Students -->
  <h1 class="page-title page-title--students">The Students</h1>

  <div class="icon-tile" role="img" aria-label="Group of students icon" style="top:66px;background:linear-gradient(var(--icon-blue) 0 55%,#9cc0e6 55%)"></div>
  <div class="icon-tile" role="img" aria-label="Graduation cap icon" style="top:345px;background:var(--icon-red)"></div>
  <div class="icon-tile" role="img" aria-label="Application form icon" style="top:558px;background:var(--icon-sky);border:3px solid #8fb6dd"></div>

  <h2 class="section-heading" style="left:745px;top:66px">Who’s it for</h2>

  <h3 class="sub-heading" style="left:745px;top:92px">High school graduates</h3>
  <ul class="bullets" style="left:745px;top:116px">
    <li>90% of high school grads aren’t sure why they’re going to university or what they want to study.</li>
    <li>VPI helps students discover what they truly want to do in life, and make enormous progress towards these goals.</li>
  </ul>

  <h3 class="sub-heading" style="left:745px;top:234px">Post-secondary students</h3>
  <ul class="bullets" style="left:745px;top:258px">
    <li>28% of students switch or drop out of their program because it wasn’t for them or they didn’t like it.</li>
    <li>Don’t keep moving around or risk switching careers down the road – find out what sparks your passion with VPI.</li>
  </ul>

  <h3 class="sub-heading" style="left:745px;top:398px">Post-secondary graduates</h3>
  <ul class="bullets" style="left:745px;top:422px">
    <li>50% of graduates are unemployed or underemployed, 60% are in debt.</li>
    <li>VPI will help you get your dream job – our students won’t settle for anything less.</li>
  </ul>

  <h2 class="section-heading" style="left:745px;top:554px">How to apply</h2>
  <ul class="bullets" style="left:745px;top:584px">
    <li>We select high-potential young leaders with a desire to improve themselves and impact the world.</li>
    <li>We won’t ask you for your grades – we care more about your values and potential.</li>
    <li>Visit www.vesk.institute to apply now</li>
  </ul>

</main>
</body>
</html>
```